Wren Motorcar Polishing Flyer Design

Hi, I need a flyer design for the pricing and package display of my business (Wren Motorcar Polishing)

www.kelvora.example/wrenmotorpolish

To keep this short and simple, I will need 2 versions of your finished product, can be similar in design just has to be saying something different.

First flyer will be the general version for all customers.

It will need to include the following!
Format, Placement, Font, Design etc.. is all up to you!

==================================

Package 1 [Cars $49.99][Trucks Vans & SUV's $54.99]: Speed Detail

- Exterior Pressure Clean w/ Spotless water
treatment and Vacuum dried
- Wheel Wells Glossed and Cleaned
- Tires Cleaned and Hand Dried
- Tires Dressed with Gloss Finish
- Exterior and Interior Windows cleaned and Hand Dried
- Interior is Vacuumed and Door jams cleaned to Perfection!

Package 2 [Cars $59.99][Trucks Vans & SUV's $64.99]: Speed Detail & Hand Waxing

- Exterior Pressure Clean w/ Spotless water treatment and Vacuum dried
- Hand Applied Wax Treatment with Delmark's Advanced Spray on wax & Micro Scratch Sealant!

Package 3 [Cars $110.00][Trucks Vans & SUV's $149.99]: Advanced Interior Detail

- Interior & Exterior Windows Cleaned and Hand Dried
- All Vents and Creases cleaned out
- Advanced plastic/vinyl/leather Vellusta Interior Treatment!
- Plastic/Vinyl/Leather Conditioner Vellusta Treatment
- Hand Treated Dust Removal
- Seats/Carpets/Headliner steam cleaned
- Seat Belts/Trunks & Floor Mats Treated and Rejuvenated
- Stain Removal

Package 4 [Cars $110.00][Trucks Vans & SUV's $149.99]: Advanced Exterior Detail

- Exterior Pressure Clean w/ Spotless water treatment and Vacuum dry with additional Hand Drying
- Hand Applied Carnauba Wax & Micro Scratch Sealant Treatment
- Dark Exterior Plastic Restoration Treatment (wherever applicable)

Package 5 [Cars $210][Trucks Vans & SUV's $299.99];The Complete Detail

- Stain Removal

Additional Options (May be applied to existing packages when requested!):

(Clay Bar Treatment): [Cars $69.99][Trucks Vans & SUV's $99.99]

- Removal of all Build-Up on Paint such as Micro debris, stone chips, water spots

(Full Vehicle Polishing): [Cars $75.99][Trucks Vans & SUV's $119.99]

- This process removes marring, swirl marks, scratches, stone chips, water spots and acid etching caused by bird droppings and bug remains.

- Adds a sleek shine when wax is applied after.

(Drop-Q Hand Applied Window Treatment): [Cars $10.00][Trucks Vans & SUV's $15]

- This process repels water, making windshield wipers unneeded during storms and rainy weather.

A percentage of proceeds will be Donated to Help Veterans in need!

Phone #: xxx-xxx-xxxx
Email #: xxxxxxxxxx
Instagram: @
Facebook: kelvora.example/wrenmotorpolish
website: > Coming Soon <

Alright, that will be the first designed flyer.

The next flyer can be single paged or flyer layed out. It is generally aimed towards my first customer Lindqvist Strength and Care. An image of there logo will be provided below along with my logo and current business card so ideas can be drawn beside them.

Wren Motorcar Polishing
The Lindqvist Special (For August)

Package 1 [Cars $24.99][Trucks Vans & SUV's $34.99]: Speed Detail

Package 2 [Cars $39.99][Trucks Vans & SUV's $44.99]: Speed Detail & Hand Waxing

Thanks a TON! If you guy's need anymore information or have any other questions during the design process, please, please; let me know!

Target Market(s)

Automotive Detailing, Mobile Automotive Detailing, Parking Lot Detailing, Business Detailing, etc.

Industry/Entity Type

Automotive

Requirements
Must have
• A Classy Design, I'd like it to match in some form or another the Card pictures I have submitted
Nice to have
• Black and White as primary colors, silver aswell
Should not have
• Not too much Wren orange coloring in the design unless it adds to the overall definition of the finished project. Thanks!

```html
<!DOCTYPE html>
<html lang="en">
<head>
<meta charset="utf-8">
<title>Wren Motorcar Polishing – The Lindqvist Special</title>
<link href="https://fonts.googleapis.com/css2?family=Lato:wght@300;400&family=Oswald:wght@400;500;600&display=swap" rel="stylesheet">
<style>
  :root{
    --page:#e9e9e7;
    --flyer-dark:#161a22;
    --flyer-mid:#272c36;
    --band:#5b5d63;
    --cell:#56585e;
    --white:#ffffff;
    --silver:#c4c6ca;
    --accent:#e8452a;
    --accent-dark:#c9341d;
    --ring:#8b8d92;
  }
  *{margin:0;padding:0;box-sizing:border-box}
  html,body{width:1200px;height:1200px;overflow:hidden;background:var(--page)}
  .flyer{
    position:absolute;left:78px;top:21px;width:1044px;height:1158px;
    background:radial-gradient(ellipse at 40% 10%,var(--flyer-mid) 0%,var(--flyer-dark) 75%);
    color:var(--white);font-family:'Lato',sans-serif;font-weight:300;overflow:hidden;
  }
  .package-band{
    position:absolute;left:0;width:467px;height:74px;background:var(--band);
    font-size:42px;font-weight:300;line-height:74px;padding-left:58px;letter-spacing:1px;
  }
  .band-1{top:13px}
  .band-2{top:528px}
  .vehicle-label{
    position:absolute;font-family:'Oswald',sans-serif;font-weight:500;font-size:29px;line-height:31px;
    transform:scaleX(.8);transform-origin:left top;
  }
  .price-badge{
    position:absolute;width:80px;height:80px;border-radius:50%;
    background:var(--accent);border:3px solid var(--white);
    box-shadow:4px 3px 0 var(--ring);
    display:flex;align-items:center;justify-content:center;
    font-family:'Oswald',sans-serif;font-weight:500;font-size:25px;
  }
  .price-badge span{display:inline-block;transform:scaleX(.82)}
  .feature-list{position:absolute;left:61px;width:400px;list-style:none}
  .feature-list li{position:absolute;left:0;font-size:15px;line-height:15.5px;white-space:nowrap}
  .feature-list li::before{
    content:"";position:absolute;left:-17px;top:1px;width:13px;height:13px;border-radius:50%;
    background:var(--accent);box-shadow:-1px 1px 0 var(--accent-dark);
  }
  .offer-title{position:absolute;left:42px;top:452px;width:420px}
  .offer-title .business-name{
    font-family:'Oswald',sans-serif;font-weight:400;font-size:26px;letter-spacing:3px;line-height:34px;
  }
  .offer-title .special-name{
    font-size:17px;font-weight:300;letter-spacing:2px;color:var(--silver);line-height:26px;
  }
  .photo-grid{
    position:absolute;left:502px;top:15px;width:359px;height:984px;
    display:grid;grid-template-columns:1fr 1fr;grid-template-rows:repeat(7,1fr);
  }
  .cell{background:var(--cell)}
  .photo{background:linear-gradient(135deg,#3a3d44,#8a8c90)}
  .photo.red{background:linear-gradient(160deg,#3b3c40 0%,#6f7075 55%,#d9432a 100%)}
  .photo.white{background:linear-gradient(160deg,#dcdfe4,#a39986)}
  .photo.light{background:linear-gradient(160deg,#8c8e92,#d6d6d4)}
  .tagline{
    position:absolute;left:975px;top:569px;width:1010px;
    transform:translate(-50%,-50%) rotate(-90deg);
    font-size:84px;font-weight:300;line-height:1;text-align:center;white-space:nowrap;letter-spacing:1px;
  }
  .donation-band{
    position:absolute;left:0;top:1052px;width:903px;height:65px;background:var(--band);
    font-size:22px;line-height:65px;padding-left:26px;white-space:nowrap;
  }
  .contact-line{
    position:absolute;left:26px;top:1128px;width:880px;
    font-size:13px;letter-spacing:1px;color:var(--silver);white-space:nowrap;
    display:flex;gap:26px;
  }
</style>
</head>
<body>
<main class="flyer">
  <section class="package package-1">
    <h2 class="package-band band-1">PACKAGE 1</h2>
    <div class="vehicle-label" style="left:42px;top:111px">CARS</div>
    <div class="price-badge" style="left:108px;top:104px"><span>$24.99</span></div>
    <div class="vehicle-label" style="left:238px;top:105px">TRUCKS<br>VANS &amp;<br>SUV's</div>
    <div class="price-badge" style="left:331px;top:104px"><span>$34.99</span></div>
    <ul class="feature-list" style="top:231px">
      <li style="top:0">Exterior Pressure Clean w/ Spotless water treatment<br>and Vacuum dried</li>
      <li style="top:40px">Wheel Wells Glossed and Cleaned</li>
      <li style="top:65px">Tires Cleaned and Hand Dried</li>
      <li style="top:90px">Tires Dressed with Gloss Finish</li>
      <li style="top:116px">Exterior and Interior Windows cleaned and Hand<br>Dried</li>
      <li style="top:156px">Interior is Vacuumed and Door jams cleaned to<br>Perfection!</li>
    </ul>
  </section>

  <header class="offer-title">
    <h1 class="business-name">WREN MOTORCAR POLISHING</h1>
    <p class="special-name">THE LINDQVIST SPECIAL (FOR AUGUST)</p>
  </header>

  <section class="package package-2">
    <h2 class="package-band band-2">PACKAGE 2</h2>
    <div class="vehicle-label" style="left:64px;top:663px">CARS</div>
    <div class="price-badge" style="left:129px;top:644px"><span>$39.99</span></div>
    <div class="vehicle-label" style="left:266px;top:644px">TRUCKS<br>VANS &amp;<br>SUV's</div>
    <div class="price-badge" style="left:358px;top:644px"><span>$44.99</span></div>
    <ul class="feature-list" style="top:770px">
      <li style="top:0">Exterior Pressure Clean w/ Spotless water treatment<br>and Vacuum dried</li>
      <li style="top:40px">Wheel Wells Glossed and Cleaned</li>
      <li style="top:65px">Tires Cleaned and Hand Dried</li>
      <li style="top:90px">Tires Dressed with Gloss Finish</li>
      <li style="top:115px">Exterior and Interior Windows cleaned and Hand Dried</li>
      <li style="top:140px">Interior is Vacuumed and Door jams cleaned to<br>Perfection!</li>
      <li style="top:181px">Hand Applied Wax Treatment with Delmark's Advanced<br>Spray on wax &amp; Micro Scratch Sealant!</li>
    </ul>
  </section>

  <div class="photo-grid">
    <div class="photo red" role="img" aria-label="Open trunk of a red hatchback after detailing"></div>
    <div class="cell"></div>
    <div class="cell"></div>
    <div class="photo white" role="img" aria-label="White sedan parked outside after a wash"></div>
    <div class="photo light" role="img" aria-label="Clean grey leather rear seats"></div>
    <div class="cell"></div>
    <div class="cell"></div>
    <div class="photo" role="img" aria-label="Detailed dashboard and centre console"></div>
    <div class="photo red" role="img" aria-label="Polished twin chrome exhaust tips"></div>
    <div class="cell"></div>
    <div class="cell"></div>
    <div class="photo red" role="img" aria-label="Cleaned engine bay"></div>
    <div class="photo" role="img" aria-label="Dark leather front seats after cleaning"></div>
    <div class="cell"></div>
  </div>

  <div class="tagline">LIVE THE DETAILS FOR US!</div>

  <div class="donation-band">A PERCENTAGE OF PROCEEDS WILL BE DONATED TO HELP VETERANS IN NEED!</div>

  <footer class="contact-line">
    <span>PHONE: xxx-xxx-xxxx</span>
    <span>FACEBOOK: kelvora.example/wrenmotorpolish</span>
    <span>WEBSITE: COMING SOON</span>
  </footer>
</main>
</body>
</html>
```